Industrial CNC laser cutting machine manufacturer needs a website designed

We need a website design for our company that re manufactures CNC laser cutting machines, we take old retired machines and completely re manufacture them from the ground up bringing them into the latest technology with all new parts and give them a new lease on life for a fraction of the cost of a new machine.

Machines can be fully customized to suit customers requirements too

My logo will need to be integrated and I want the website to look clean and modern

I will probably want 4 pages,Home, pictures, machines for sale and contact

```html
<!DOCTYPE html>
<html lang="en">
<head>
<meta charset="utf-8">
<title>Beamline Machine Works – CNC Laser Cutting Machines</title>
<link rel="stylesheet" href="https://fonts.googleapis.com/css2?family=Rajdhani:wght@500;600;700&family=Mulish:wght@400;600;700&display=swap">
<style>
:root{
  --red:#ed1c24;
  --ink:#222226;
  --text:#555;
  --muted:#777;
  --band:#e6e6e6;
  --white:#fff;
  --footer:#2b2b2e;
  --footer-text:#a9a9ad;
  --head:'Rajdhani',sans-serif;
  --body:'Mulish',sans-serif;
}
*{box-sizing:border-box;margin:0;padding:0}
html,body{width:1200px;height:4051px;overflow:hidden}
body{position:relative;background:var(--white);font-family:var(--body);color:var(--text)}
.abs{position:absolute}
.photo{position:absolute}

/* header */
.site-header{position:absolute;left:0;top:0;width:1200px;height:84px;background:var(--white)}
.brand{position:absolute;left:94px;top:24px;display:flex;align-items:center;gap:10px;font-family:var(--head);font-weight:700;font-size:22px;color:var(--red);letter-spacing:1px}
.brand-mark{width:32px;height:32px;background:var(--ink)}
.nav{position:absolute;top:25px;left:703px;display:flex;font-size:13px;color:var(--ink)}
.nav a{display:block;height:38px;line-height:38px;text-decoration:none;color:inherit}
.nav .active{border:1px solid var(--red);color:var(--red);width:80px;text-align:center;margin-right:28px}
.nav a:nth-child(2){margin-right:50px}
.nav a:nth-child(3){margin-right:54px}

/* hero */
.hero{position:absolute;left:0;top:84px;width:1200px;height:554px;background:radial-gradient(ellipse at 62% 45%,#c88a3a 0%,#5a4030 18%,#1b2236 45%,#0b1020 100%)}
.hero-kicker{position:absolute;left:112px;top:186px;font-size:24px;color:var(--white);font-family:var(--body)}
.hero-title{position:absolute;left:110px;top:214px;font-family:var(--head);font-weight:700;font-size:66px;color:var(--white);line-height:1}
.btn{display:inline-block;background:var(--red);color:var(--white);font-family:var(--body);font-weight:700;font-size:14px;text-align:center}
.hero .btn{position:absolute;left:115px;top:308px;width:158px;height:45px;line-height:45px}
.dots span{position:absolute;left:1093px;width:12px;height:12px;border-radius:50%;border:1.5px solid var(--white)}
.dots .on{background:var(--red);border-color:var(--red)}

/* features */
.features{position:absolute;left:0;top:638px;width:1200px;height:195px}
.feature{position:absolute;top:60px;width:240px}
.feature-icon{position:absolute;left:0;top:4px;width:70px;height:70px;border-radius:6px;background:linear-gradient(135deg,#f5b43a,#e85a2c)}
.feature h3{position:absolute;left:82px;top:0;font-family:var(--head);font-weight:700;font-size:15px;color:var(--ink)}
.feature p{position:absolute;left:82px;top:22px;width:158px;font-size:11.5px;line-height:18px;color:var(--muted)}

/* welcome */
.welcome{position:absolute;left:0;top:833px;width:1200px;height:444px;background:var(--band)}
.welcome .kicker{position:absolute;left:94px;top:100px;font-size:20px;color:var(--red)}
.welcome h2{position:absolute;left:94px;top:120px;font-family:var(--head);font-weight:700;font-size:35px;color:var(--ink)}
.welcome p{position:absolute;left:94px;top:172px;width:460px;font-size:12.5px;line-height:19.5px;color:var(--text)}
.welcome .btn{position:absolute;left:94px;top:291px;width:139px;height:45px;line-height:45px}
.welcome-frame{position:absolute;left:633px;top:21px;width:472px;height:378px;background:var(--red);border-radius:60px 0 28px 0}
.welcome-photo{left:602px;top:46px;width:473px;height:380px;background:linear-gradient(160deg,#d9d9d6 0%,#b7b3ad 45%,#e4823a 70%,#8a857e 100%);border-radius:0 0 40px 0}

/* machines */
.section-title{position:absolute;left:0;width:1200px;text-align:center;font-family:var(--head);font-weight:700;font-size:34px;color:var(--ink)}
.card{position:absolute;top:1388px;width:236px}
.card-photo{position:relative;width:236px;height:271px;background:linear-gradient(170deg,#cfcfcc 0%,#ea7a2e 55%,#7c6e62 100%)}
.card h3{margin-top:14px;font-family:var(--head);font-weight:700;font-size:16px;color:var(--ink)}
.card p{margin-top:4px;font-size:12px;line-height:18.5px;color:var(--muted)}
.card a{display:block;margin-top:10px;font-size:11px;font-weight:700;color:var(--red);text-decoration:none}
.arrow{position:absolute;top:1488px;width:36px;height:80px}

/* video */
.video{position:absolute;left:0;top:1836px;width:1200px;height:442px;background:linear-gradient(180deg,#cdd0d2 0%,#9a9a98 40%,#4a3a30 60%,#2a2a2a 100%)}
.video h2{position:absolute;left:0;top:246px;width:1200px;text-align:center;font-family:var(--head);font-weight:600;font-size:34px;color:var(--white)}

/* gallery */
.tile{position:absolute}
.btn-outline{position:absolute;left:521px;top:2831px;width:158px;height:45px;line-height:43px;border:1.5px solid var(--red);color:var(--red);text-align:center;font-weight:700;font-size:14px}

/* contact */
.contact{position:absolute;left:0;top:2936px;width:1200px;height:504px;background:var(--band)}
.contact-card{position:absolute;left:94px;top:94px;width:335px;height:310px;background:var(--red);color:var(--white);padding:26px 19px;border-radius:4px}
.contact-card h3{font-family:var(--head);font-weight:700;font-size:22px;margin-top:0}
.contact-card h4{font-family:var(--head);font-weight:700;font-size:16px;margin-top:24px}
.info{display:flex;gap:8px;font-size:12px;line-height:19px;margin-top:14px}
.info svg{flex:none;margin-top:3px}
.socials{display:flex;gap:4px;margin-top:10px}
.socials span{width:29px;height:29px;border:1px solid var(--white)}
.form h3{position:absolute;left:457px;top:112px;font-family:var(--head);font-weight:700;font-size:22px;color:var(--ink)}
.field{position:absolute;background:var(--white);border:1px solid #cfcfcf;font-size:13px;color:#777;padding:10px 6px}
.form .btn{position:absolute;left:457px;top:364px;width:140px;height:44px;line-height:44px}

/* clients */
.client{position:absolute;top:3535px;width:110px;text-align:center;font-family:var(--head);font-weight:700;font-size:15px;color:#666;letter-spacing:1px}
.client span{display:block;width:54px;height:54px;margin:0 auto 8px;border-radius:50%;background:#8a8a8a}

/* footer */
.footer{position:absolute;left:0;top:3664px;width:1200px;height:387px;background:var(--footer);color:var(--footer-text);font-size:12px}
.fcol{position:absolute;top:78px}
.fcol h4{font-family:var(--head);font-weight:700;font-size:17px;color:var(--white);margin-bottom:20px}
.fcol li{list-style:none;line-height:31px}
.fcol .info{margin-top:12px}
.f-socials{display:flex;gap:6px;margin-top:16px}
.f-socials span{width:26px;height:26px;border:1px solid #888}
.sub-input{width:245px;height:36px;background:var(--white);margin-top:12px;color:#888;font-size:11px;padding:11px 12px}
.sub-btn{margin:12px 0 0 145px;width:100px;height:36px;line-height:36px}
.copy{position:absolute;left:0;top:354px;width:1200px;text-align:center;font-size:11px}
.copy em{font-style:normal;color:var(--red)}
</style>
</head>
<body>

<header class="site-header">
  <div class="brand"><span class="brand-mark"></span>BEAMLINE MACHINE WORKS</div>
  <nav class="nav">
    <a class="active">Home</a><a>Pictures</a><a>Machines for sale</a><a>Contact</a>
  </nav>
</header>

<section class="hero" role="img" aria-label="Laser cutting head firing sparks onto a metal sheet">
  <p class="hero-kicker">Manufactures CNC laser</p>
  <h1 class="hero-title">Cutting Machines</h1>
  <span class="btn">Know More</span>
  <div class="dots"><span class="on" style="top:240px"></span><span style="top:270px"></span><span style="top:300px"></span></div>
</section>

<section class="features">
  <div class="feature" style="left:94px"><div class="feature-icon" role="img" aria-label="Laser head illustration"></div><h3>Unique</h3><p>Lorem ipsum dolor sit amet, consetur adipiscing elit. Quisque libero metus</p></div>
  <div class="feature" style="left:356px"><div class="feature-icon" role="img" aria-label="Quality machinery illustration"></div><h3>High Quality</h3><p>Lorem ipsum dolor sit amet, consetur adipiscing elit. Quisque libero metus</p></div>
  <div class="feature" style="left:618px"><div class="feature-icon" role="img" aria-label="Service technician illustration"></div><h3>Service</h3><p>Lorem ipsum dolor sit amet, consetur adipiscing elit. Quisque libero metus</p></div>
  <div class="feature" style="left:880px"><div class="feature-icon" role="img" aria-label="Factory manufacturing illustration"></div><h3>Manufacturer</h3><p>Lorem ipsum dolor sit amet, consetur adipiscing elit. Quisque libero metus</p></div>
</section>

<section class="welcome">
  <p class="kicker">Welcome to</p>
  <h2>Beamline Machine Works</h2>
  <p>Lorem ipsum dolor sit amet, consectetur adipiscing elit. Quisque libero metus, laoreet vel orci accumsan, vulputate ultrices libero. Vestibulum vel tortor at ipsum facilisis iaculis. Proin conectetur eget nunc sit amet fringilla. Curabitur in sollicitudin velit, eget aliquet enim. Etiam aliquam auctor ante, vitae dignissim quam rhoncus id.</p>
  <span class="btn">Read More</span>
  <div class="welcome-frame"></div>
  <div class="photo welcome-photo" role="img" aria-label="Orange laser cutting machine bed in a workshop"></div>
</section>

<h2 class="section-title" style="top:1324px">Machines For Sale</h2>
<article class="card" style="left:94px"><div class="card-photo" role="img" aria-label="Enclosed orange CNC machine"></div><h3>CNC Router Pro</h3><p>Proin conectetur eget nunc sit amet fringilla. Curabitur in sollicitudin velit, eget aliquet enim.</p><a>Read More</a></article>
<article class="card" style="left:353px"><div class="card-photo" role="img" aria-label="Fiber laser machine frame"></div><h3>Fiber Laser Marking Machine</h3><p>Proin conectetur eget nunc sit amet fringilla. Curabitur in sollicitudin velit, eget aliquet enim.</p><a>Read More</a></article>
<article class="card" style="left:612px"><div class="card-photo" role="img" aria-label="Laser marking machine in workshop"></div><h3>3D Laser Marking Machine</h3><p>Proin conectetur eget nunc sit amet fringilla. Curabitur in sollicitudin velit, eget aliquet enim.</p><a>Read More</a></article>
<article class="card" style="left:870px"><div class="card-photo" role="img" aria-label="Enclosed robotic laser cutter"></div><h3>Robotic Laser Cutting Machine</h3><p>Proin conectetur eget nunc sit amet fringilla. Curabitur in sollicitudin velit, eget aliquet enim.</p><a>Read More</a></article>
<svg class="arrow" style="left:76px" viewBox="0 0 36 80"><rect width="36" height="80" fill="#555" opacity=".7"/><path d="M22 24 L12 40 L22 56" fill="none" stroke="#fff" stroke-width="1.5"/></svg>
<svg class="arrow" style="left:1089px" viewBox="0 0 36 80"><rect width="36" height="80" fill="#ed1c24"/><path d="M14 24 L24 40 L14 56" fill="none" stroke="#fff" stroke-width="1.5"/></svg>

<section class="video" role="img" aria-label="Laser cutting machine gantry inside workshop">
  <svg class="abs" style="left:564px;top:169px" width="72" height="72" viewBox="0 0 72 72"><circle cx="36" cy="36" r="34" fill="none" stroke="#fff" stroke-width="2.5"/><path d="M29 23 L49 36 L29 49 Z" fill="none" stroke="#fff" stroke-width="2.5" stroke-linejoin="round"/></svg>
  <h2>Work Procedure</h2>
</section>

<div class="tile" style="left:94px;top:2330px;width:336px;height:240px;background:linear-gradient(160deg,#5b5f70,#1d2340 60%,#c44a3a)" role="img" aria-label="Laser nozzle close-up"></div>
<div class="tile" style="left:768px;top:2330px;width:338px;height:240px;background:linear-gradient(170deg,#d8d8d4,#f1f1ef 50%,#e2722a)" role="img" aria-label="White and orange machine enclosure"></div>
<div class="tile" style="left:94px;top:2570px;width:336px;height:236px;background:linear-gradient(150deg,#e46e28,#6a5a52 60%,#3a3a3a)" role="img" aria-label="Machine cabling detail"></div>
<div class="tile" style="left:430px;top:2570px;width:338px;height:236px;background:radial-gradient(circle at 50% 60%,#f4c27a,#5a4636 40%,#141414 80%)" role="img" aria-label="Sparks from cutting"></div>
<div class="tile" style="left:768px;top:2570px;width:338px;height:236px;background:linear-gradient(160deg,#d9d9d6,#e36e26 50%,#4e4e4e)" role="img" aria-label="Machine rail and gantry"></div>
<div class="tile" style="left:405px;top:2314px;width:388px;height:266px;background:linear-gradient(170deg,#9a9a98 0%,#e2621f 25%,#c9551c 100%);box-shadow:0 6px 20px rgba(0,0,0,.45)" role="img" aria-label="Orange machine cabinet front">
  <svg class="abs" style="left:172px;top:118px" width="44" height="44" viewBox="0 0 44 44"><path d="M4 40 L40 4 M26 4 H40 V18 M4 26 V40 H18" fill="none" stroke="#fff" stroke-width="2"/></svg>
</div>
<span class="btn-outline">View All Images</span>

<section class="contact">
  <h2 class="section-title" style="top:34px">Get In Touch</h2>
  <div class="contact-card">
    <h3>Contact Info</h3>
    <div class="info"><svg width="12" height="14" viewBox="0 0 12 14"><path d="M6 0C2.7 0 0 2.6 0 5.8 0 10 6 14 6 14s6-4 6-8.2C12 2.6 9.3 0 6 0z" fill="#fff"/><circle cx="6" cy="5.8" r="2" fill="#ed1c24"/></svg><span>12 Foundry Lane,<br>Riverton East</span></div>
    <div class="info"><svg width="12" height="12" viewBox="0 0 12 12"><path d="M2.5 0.5 L4.5 3 L3.5 4.5 Q5 7.5 7.5 8.5 L9 7.5 L11.5 9.5 L10 11.5 Q4 11 0.5 2 Z" fill="#fff"/></svg><span>info@beamlineworks.example</span></div>
    <div class="info"><svg width="13" height="10" viewBox="0 0 13 10"><rect width="13" height="10" fill="#fff"/><path d="M0 0 L6.5 5.5 L13 0" fill="none" stroke="#ed1c24"/></svg><span>02-555-018-274</span></div>
    <h4>Follow Us</h4>
    <div class="socials"><span></span><span></span><span></span><span></span></div>
  </div>
  <div class="form">
    <h3>Contact us</h3>
    <div class="field" style="left:457px;top:150px;width:320px;height:42px">Name</div>
    <div class="field" style="left:785px;top:150px;width:321px;height:42px">Email</div>
    <div class="field" style="left:457px;top:202px;width:320px;height:42px">Phone</div>
    <div class="field" style="left:785px;top:202px;width:321px;height:42px">Subject</div>
    <div class="field" style="left:457px;top:254px;width:649px;height:93px">Your Message</div>
    <span class="btn">Send Now</span>
  </div>
</section>

<h2 class="section-title" style="top:3472px">Our Prestigious Clients</h2>
<div class="client" style="left:76px"><span></span>NORVANE</div>
<div class="client" style="left:275px"><span></span>KESTREL</div>
<div class="client" style="left:476px"><span></span>ALDERMOOR</div>
<div class="client" style="left:677px"><span></span>CORVEX</div>
<div class="client" style="left:876px"><span></span>TALLIS</div>
<div class="client" style="left:1020px"><span></span>BRIGHTFOLD</div>

<footer class="footer">
  <div class="fcol" style="left:94px">
    <h4>Contact Us</h4>
    <div class="info"><svg width="12" height="14" viewBox="0 0 12 14"><path d="M6 0C2.7 0 0 2.6 0 5.8 0 10 6 14 6 14s6-4 6-8.2C12 2.6 9.3 0 6 0z" fill="#ed1c24"/></svg><span>12 Foundry Lane,<br>Riverton East</span></div>
    <div class="info"><svg width="12" height="12" viewBox="0 0 12 12"><path d="M2.5 0.5 L4.5 3 L3.5 4.5 Q5 7.5 7.5 8.5 L9 7.5 L11.5 9.5 L10 11.5 Q4 11 0.5 2 Z" fill="#ed1c24"/></svg><span>info@beamlineworks.example</span></div>
    <div class="info"><svg width="13" height="10" viewBox="0 0 13 10"><rect width="13" height="10" fill="#ed1c24"/><path d="M0 0 L6.5 5.5 L13 0" fill="none" stroke="#2b2b2e"/></svg><span>02-555-018-274</span></div>
    <div class="f-socials"><span></span><span></span><span></span><span></span></div>
  </div>
  <div class="fcol" style="left:415px"><h4>Quick Links</h4><ul><li>Home</li><li>Pictures</li><li>Machines for sale</li><li>Contact</li></ul></div>
  <div class="fcol" style="left:629px"><h4>Products</h4><ul><li>Aliquam hendrerit comentum</li><li>Pharetra nequesce ultrices</li><li>Quam sed magna cursus</li><li>Donec dapibus sem vitae</li><li>Aliquam a sapien placerat</li></ul></div>
  <div class="fcol" style="left:861px"><h4>Subscribe</h4><p>Access exclusive offers news and more</p><div class="sub-input">Enter your email address</div><div class="btn sub-btn">Subscribe</div></div>
  <p class="copy">© 2020 <em>Beamline Machine Works</em>. All Right Reserved.</p>
</footer>

</body>
</html>
```